Legal firm website redesign

Existing site for Sydney CBD lawyer needs clean and professional redesign - http://brennicklaw.com.au

The site will be viewed by a wide range of users: businesses, individuals, referral partners and other lawyers.

Please see the list of must haves for further details

Target Market(s)

Businesses, individuals, referral partners and other lawyers

Industry/Entity Type

Lawyer

Requirements
Must have
• Prominent display of phone number.
List of services down the left hand side of the site (5x services or so).
Search box in header.
Please use the greys and blues from the existing header.
New header must include the wording "Efficiency - Fulfillment - Integrity - Teamwork"

```html
<!DOCTYPE html>
<html lang="en">
<head>
<meta charset="utf-8">
<title>Brennick Law</title>
<link rel="stylesheet" href="https://fonts.googleapis.com/css2?family=Libre+Baskerville:wght@700&family=Roboto+Condensed:wght@400;700&family=Arimo:wght@400&display=swap">
<style>
:root{
  --blue:#1f6fcf;
  --blue-light:#4a9be8;
  --blue-dark:#1a62c0;
  --heading-blue:#1b5fb3;
  --sidebar:#474747;
  --sidebar-line:#5c5c5c;
  --text:#1e1e1e;
  --muted:#555;
  --border:#cfcfcf;
  --gold:#f3c86a;
}
*{box-sizing:border-box;margin:0;padding:0}
html,body{width:1200px;height:912px;overflow:hidden}
body{position:relative;background:linear-gradient(#fafafa,#ececec 60%,#f3f3f3);font-family:"Arimo",Arial,sans-serif;color:var(--text)}
.brand{position:absolute;left:147px;top:30px;font-family:"Libre Baskerville",Georgia,serif;font-weight:700;font-size:33px;color:#2b2b2b;letter-spacing:-.5px}
.phone{position:absolute;right:145px;top:16px;font-family:"Libre Baskerville",Georgia,serif;font-weight:700;font-size:23px;color:var(--blue)}
.search{position:absolute;left:867px;top:60px;width:188px;height:30px;border:1px solid #ddd;border-radius:3px;background:#fff;font-size:12px;padding:9px 0 0 13px;color:#222}
.search svg{position:absolute;right:9px;top:7px}
.nav{position:absolute;left:145px;top:108px;width:910px;height:37px;background:linear-gradient(var(--blue-light),var(--blue-dark));display:flex}
.nav a{font-family:"Roboto Condensed",Arial,sans-serif;font-size:15px;color:#fff;text-decoration:none;line-height:37px;text-align:center;border-right:1px solid rgba(255,255,255,.45)}
.services{position:absolute;left:145px;top:159px;width:226px;height:329px;background:var(--sidebar);color:#fff}
.services h2{font-family:"Roboto Condensed",Arial,sans-serif;font-weight:400;font-size:16px;padding:18px 14px 0;height:54px;border-bottom:1px solid var(--sidebar-line)}
.services li{list-style:none;font-size:12px;padding:7px 0 7px 30px;border-bottom:1px solid var(--sidebar-line);position:relative;line-height:1.2}
.services li::before{content:"→";position:absolute;left:14px;font-size:10px;top:8px}
.services .all{position:absolute;right:16px;bottom:12px;font-size:12px}
.hero{position:absolute;left:386px;top:159px;width:669px;height:329px;border:1px solid var(--border);padding:2px;background:#fff}
.hero-art{width:100%;height:100%;background:radial-gradient(ellipse at 40% 45%,#a0662a,#4a2a18 55%,#2a1a12);position:relative}
.tagline{position:absolute;left:0;right:0;bottom:16px;text-align:center;font-family:"Libre Baskerville",Georgia,serif;font-weight:700;font-size:22px;color:#fff;text-shadow:2px 2px 3px #000}
.follow{position:absolute;left:146px;top:498px;font-family:"Roboto Condensed",Arial,sans-serif;font-size:18px;color:var(--heading-blue)}
.social{position:absolute;left:147px;top:524px;display:flex;gap:16px}
.social span{width:30px;height:30px;border-radius:4px;background:#333}
.rule{position:absolute;left:145px;top:562px;width:226px;border-top:1px solid #d6d6d6}
.aside-note{position:absolute;left:146px;top:582px;font-family:"Roboto Condensed",Arial,sans-serif;font-size:14px;line-height:23px;color:#333}
.welcome{position:absolute;left:384px;top:503px;width:672px}
.welcome h2{font-family:"Roboto Condensed",Arial,sans-serif;font-weight:400;font-size:18px;color:var(--heading-blue);margin-bottom:11px}
.welcome p{font-size:11.4px;line-height:23px;margin-bottom:10px}
.recent{position:absolute;left:145px;top:714px;width:910px;height:136px;border:1px solid var(--border);background:linear-gradient(#fff,#f2f2f2)}
.recent h2{font-family:"Roboto Condensed",Arial,sans-serif;font-weight:400;font-size:18px;color:var(--heading-blue);position:absolute;left:10px;top:11px}
.recent ul{position:absolute;top:40px;list-style:none;font-size:11.2px;line-height:22.5px}
.footer-links{position:absolute;top:860px;left:0;width:1200px;text-align:center;font-size:11.5px;color:var(--muted)}
.copyright{position:absolute;top:884px;left:0;width:1200px;text-align:center;font-size:11.5px;color:var(--muted)}
</style>
</head>
<body>
<div class="brand">Brennick Law</div>
<div class="phone">Call Us : (02) 9467 3082</div>
<div class="search">Search
  <svg width="16" height="16" viewBox="0 0 16 16"><circle cx="6" cy="6" r="4.5" fill="none" stroke="#333" stroke-width="1.6"/><line x1="9.5" y1="9.5" x2="14.5" y2="14.5" stroke="#333" stroke-width="2"/></svg>
</div>
<nav class="nav">
  <a style="width:98px">HOME</a><a style="width:120px">ABOUT US</a><a style="width:150px">AREAS OF LAW</a><a style="width:141px">PUPLICATIONS</a><a style="width:108px">CONTACT</a>
</nav>
<aside class="services">
  <h2>SERVICES</h2>
  <ul>
    <li>Financing</li><li>Leasing</li><li>Property transactions</li><li>Joint ventures</li><li>Business restructuring</li><li>Contract review and advice</li>
    <li style="border:0;padding-top:9px">Employment Law Documentation,<br>e.g. AWAs</li>
  </ul>
  <div class="all">→→ View all services</div>
</aside>
<div class="hero">
  <div class="hero-art" role="img" aria-label="Golden scales of justice and a wooden gavel before shelves of law books">
    <div class="tagline">Efficiency - Fulfillment - Integrity - Teamwork</div>
  </div>
</div>
<div class="follow">FOLLOW</div>
<div class="social" aria-label="Social links"><span></span><span></span><span></span></div>
<div class="rule"></div>
<div class="aside-note">Buying and selling businesses<br>and companies</div>
<section class="welcome">
  <h2>WELCOME</h2>
  <p>Brennick Law is a dynamic commercial law firm in the CBD of Sydney providing services to corporate, small business and private clients.</p>
  <p>Brennick Law brings together over 30 years of experience in legal practice.</p>
  <p>The strong focus of the firm is on commercial law and estate planning.</p>
  <p>Brennick Law is committed to providing quality legal services in helping its clients achieve their objectives by providing a proactive understanding of its clients' businesses and creative legal solutions.</p>
</section>
<section class="recent">
  <h2>RECENT ADITIONS</h2>
  <ul style="left:10px"><li>Commencement of the Succession Act 2006 25.03.08</li><li>Is that will valid? 15.01.08</li><li>Labor's proposed changes to IR laws 14.12.07</li><li>Should you make your own will? 14.11.07</li></ul>
  <ul style="left:319px"><li>Illegal workers 14.08.07</li><li>Employees' liability for misleading or deceptive conduct 14.08.07</li><li>Correct use of ACNs and ABNs 14.08.07</li><li>Power of Attorney Infosheet 10.08.07</li></ul>
  <ul style="left:668px"><li>Intestate Estates Infosheet 08.08.07</li><li>Estate Planning Infosheet 07.06.07</li><li>Special Disability Trusts Infosheet 18.05.07</li><li>Testamentary Trusts Infosheet 17.05.07</li></ul>
</section>
<div class="footer-links">Home | about us &nbsp;| Areas of law | Publications | Contact</div>
<div class="copyright">© 2012 brennicklaw.com.au. All Rights Reserved</div>
</body>
</html>
```